New florist business website design

Number 1 want is an easy to navigate & check out website
Needs to be beautiful and eye catching as well.
This is an online only business (no shop front)
Rustic and blush pinks, neutrals, woods, leaves
Customers need to be able to go onto my website, select something they want to buy but have the option to use a drop down box to change colours of the flowers, or add notes to make changes to the arrangement

Industry/Entity Type

Florist

Coding

Coded - Design and coding required

Number of Pages Required

5+ page

Colors
f9d9e8
fff2ec
fffefc

Requirements
Must have
• Drop down menu to take you to other pages for Arrangements, bouquets, everlasting arrangements, gifts, contact
Be able to purchase and “add to basket”
Checkout page
Nice to have
• Be able to add my own photos once I’ve taken new ones
Should not have
• Tacky images or clip art

```html
<!DOCTYPE html>
<html lang="en">
<head>
<meta charset="utf-8">
<title>Fern&amp;Vale — Florist</title>
<link rel="stylesheet" href="https://fonts.googleapis.com/css2?family=Cormorant+SC:wght@400;500;600&family=Roboto:wght@300;400&display=swap">
<style>
:root{
  --blush:#f9d9e8;
  --blush-soft:#fbe3ec;
  --peach:#fff2ec;
  --cream:#fffefc;
  --band:#fdf0ec;
  --clay:#ecccbf;
  --ink:#222;
  --text:#3a3a3a;
  --muted:#8b8b8b;
  --faint:#b8b1ae;
  --gold:#f4b400;
  --black:#0b0b0b;
  --rose:#e48cb2;
}
*{margin:0;padding:0;box-sizing:border-box}
html,body{width:1200px;height:4566px;overflow:hidden}
body{position:relative;background:var(--cream);font-family:"Roboto",Arial,sans-serif;color:var(--text)}
.abs{position:absolute}
.serif{font-family:"Cormorant SC","Times New Roman",serif}
.photo{position:absolute}
.eyebrow{position:absolute;font-family:"Cormorant SC",serif;font-size:13px;color:#555;display:flex;align-items:center;gap:6px}
.eyebrow::before{content:"";width:58px;height:1px;background:#555;display:block}
.h-title{position:absolute;font-family:"Cormorant SC",serif;font-weight:500;color:var(--ink);letter-spacing:.5px}
.para{position:absolute;font-size:12.5px;line-height:25px;color:var(--muted);font-weight:300}
.btn{position:absolute;background:var(--blush);color:#444;font-size:14px;display:flex;align-items:center;justify-content:center}
/* hero */
.hero{position:absolute;left:0;top:0;width:1200px;height:576px;background:linear-gradient(90deg,#f1f1f1 0%,#ececec 60%,#e6e4e4 100%)}
.brand{position:absolute;display:flex;align-items:center;gap:8px;font-family:"Cormorant SC",serif;font-weight:500;font-size:26px;color:#444}
.brand .dot{width:10px;height:10px;border-radius:50%;border:1px solid #666}
.nav a{position:absolute;top:59px;font-size:12.5px;color:#333;text-decoration:none}
.nav a.active::after{content:"";position:absolute;left:0;right:0;bottom:-6px;height:1px;background:#333}
/* products */
.card-img{position:absolute;width:262px;height:251px}
.card-name{position:absolute;width:262px;text-align:center;font-family:"Cormorant SC",serif;font-size:15px;font-weight:500;color:#333}
.price{position:absolute;font-size:18px;color:#222}
.price small{font-size:13px;margin-right:4px}
.stars{position:absolute;display:flex;gap:1px}
/* events */
.ev-img{position:absolute;width:192px;height:240px}
.ev-name{position:absolute;font-family:"Cormorant SC",serif;font-size:15px;font-weight:500;color:#333}
.ev-desc{position:absolute;font-size:11px;line-height:18px;color:var(--faint);width:190px;font-weight:300}
.circle-btn{position:absolute;width:30px;height:30px;border-radius:50%;display:flex;align-items:center;justify-content:center}
.pink-block{position:absolute;background:var(--peach)}
/* footer */
.footer{position:absolute;left:0;top:4195px;width:1200px;height:371px;background:var(--black);color:#fff}
.footer .f-link{position:absolute;font-size:12.5px;color:#fff}
.footer .f-head{position:absolute;font-size:15px;color:#fff}
</style>
</head>
<body>

<!-- HERO -->
<section class="hero">
  <div class="photo" role="img" aria-label="Smiling florist in an apron holding a large mixed bouquet beside flower shelves" style="left:674px;top:0;width:526px;height:576px;background:linear-gradient(135deg,#f3eeec 0%,#e8d9d4 35%,#d9c6bd 60%,#f0d9dc 100%)"></div>
  <div class="photo" role="img" aria-label="Red and yellow tulips with green leaves" style="left:0;top:222px;width:168px;height:345px;background:linear-gradient(180deg,#eab07a 0%,#9cc46e 45%,#6ea84a 100%);opacity:.75;border-radius:0 80px 0 0"></div>

  <div class="brand" style="left:190px;top:48px"><span class="dot"></span>Fern&amp;Vale</div>
  <nav class="nav">
    <a class="active" href="#" style="left:413px">Home</a>
    <a href="#" style="left:484px">About Us</a>
    <a href="#" style="left:571px">Bouquets</a>
    <a href="#" style="left:661px">Events</a>
    <a href="#" style="left:736px">Contact Us</a>
  </nav>
  <svg class="abs" style="left:693px;top:21px" width="18" height="18" viewBox="0 0 18 18" fill="none" stroke="#222" stroke-width="1.5"><circle cx="7.5" cy="7.5" r="5.5"/><path d="M12 12l4.5 4.5"/></svg>
  <svg class="abs" style="left:732px;top:21px" width="18" height="18" viewBox="0 0 18 18" fill="none" stroke="#222" stroke-width="1.5"><circle cx="9" cy="9" r="7.5"/><circle cx="9" cy="7" r="2.5"/><path d="M4 14c1.5-2.5 8.5-2.5 10 0"/></svg>
  <svg class="abs" style="left:771px;top:21px" width="20" height="18" viewBox="0 0 20 18" fill="none" stroke="#222" stroke-width="1.5"><path d="M1 2h3l2 9h9l2-7H5"/><circle cx="7" cy="15" r="1.3"/><circle cx="14" cy="15" r="1.3"/></svg>

  <div class="eyebrow" style="left:184px;top:191px">Welcome</div>
  <h1 class="h-title" style="left:182px;top:216px;font-size:47px;line-height:56px;font-weight:500">Shop Online Your<br>Favorite Bouquets.</h1>
  <p class="para" style="left:184px;top:357px;width:420px">Lorem ipsum dolor sit amet, consectetur adipiscing elit, sed do eius mod tempor incididunt ut labore et dolore magna aliqua.</p>
  <div class="btn" style="left:183px;top:445px;width:141px;height:48px">Read More</div>
  <div class="circle-btn" style="left:347px;top:446px;width:45px;height:45px;background:var(--blush)">
    <svg width="20" height="18" viewBox="0 0 20 18" fill="none" stroke="#333" stroke-width="1.4"><path d="M2 6h16l-2 10H4z"/><path d="M6 6l3-4M14 6l-3-4"/><path d="M8 10v3M12 10v3"/></svg>
  </div>
  <div class="abs" style="left:406px;top:461px;font-size:14px;color:#333">Shop Now</div>
</section>

<!-- ABOUT -->
<section>
  <div class="photo" role="img" aria-label="Pink and magenta roses arranged in a wooden crate" style="left:183px;top:667px;width:333px;height:450px;background:linear-gradient(160deg,#6f6a5e 0%,#c44b7a 35%,#e9c2c6 65%,#9aa08f 100%)"></div>
  <div class="pink-block" style="left:516px;top:693px;width:92px;height:108px"></div>
  <div class="abs" style="left:316px;top:775px;width:266px;height:344px;background:#fff"></div>
  <div class="photo" role="img" aria-label="Woman in a black hat holding yellow chrysanthemums against a pink wall" style="left:324px;top:783px;width:258px;height:336px;background:linear-gradient(180deg,#f0707f 0%,#ec6f80 45%,#f1d23c 70%,#efeae4 100%)"></div>

  <div class="eyebrow" style="left:626px;top:785px">About Us</div>
  <h2 class="h-title" style="left:626px;top:812px;font-size:29px;line-height:42px">Your Events Flowers<br>Specialist</h2>
  <p class="para" style="left:626px;top:914px;width:290px">Ut enim ad minim veniam, quis nostrud exerci tation ullamco laboris nisi ut aliquip ex ea commodo consequat. Duis aute irure dolor in reprehenderit in voluptate velit esse cillum dolore eu fugiat nulla pariatur.</p>
  <div class="btn" style="left:626px;top:1069px;width:145px;height:50px">Know More</div>
</section>

<!-- BESTSELLERS -->
<section>
  <div class="eyebrow" style="left:536px;top:1206px">Bouquets</div>
  <h2 class="h-title" style="left:0;width:1200px;text-align:center;top:1234px;font-size:29px">Send Our Bestsellers For Every Occasion</h2>

  <!-- row 1 -->
  <div class="card-img" role="img" aria-label="Pink bouquet on a blush background" style="left:183px;top:1330px;background:linear-gradient(180deg,#f7c1cf,#f4b4c6)"></div>
  <div class="abs" style="left:223px;top:1369px;width:181px;height:164px;border:3px solid #fff;background:rgba(255,255,255,.15)"></div>
  <div class="circle-btn" style="left:236px;top:1421px;width:38px;height:38px;background:#fff"><svg width="16" height="14" viewBox="0 0 16 14" fill="none" stroke="#333" stroke-width="1.3"><path d="M8 13S1 8.5 1 4.5A3.3 3.3 0 0 1 8 3a3.3 3.3 0 0 1 7 1.5C15 8.5 8 13 8 13z"/></svg></div>
  <div class="circle-btn" style="left:295px;top:1421px;width:38px;height:38px;background:#fff"><svg width="17" height="15" viewBox="0 0 20 18" fill="none" stroke="#333" stroke-width="1.5"><path d="M1 2h3l2 9h9l2-7H5"/><circle cx="7" cy="15" r="1.3"/><circle cx="14" cy="15" r="1.3"/></svg></div>
  <div class="circle-btn" style="left:353px;top:1421px;width:38px;height:38px;background:#fff"><svg width="18" height="14" viewBox="0 0 18 14" fill="none" stroke="#333" stroke-width="1.3"><path d="M1 7s3-5 8-5 8 5 8 5-3 5-8 5-8-5-8-5z"/><circle cx="9" cy="7" r="2.3"/></svg></div>
  <div class="abs serif" style="left:223px;top:1488px;width:181px;text-align:center;font-size:14px;color:#555">View Details</div>
  <div class="card-name" style="left:183px;top:1592px">Heirloom Opulence</div>
  <div class="price" style="left:189px;top:1621px"><small>$</small>12.65</div>

  <div class="card-img" role="img" aria-label="Pink tulips wrapped in kraft paper with a ribbon" style="left:468px;top:1330px;background:linear-gradient(180deg,#f1c9b7,#edc0ac)"></div>
  <div class="card-name" style="left:468px;top:1592px">Delectable Pink</div>
  <div class="price" style="left:474px;top:1621px"><small>$</small>15.00</div>

  <div class="card-img" role="img" aria-label="Red and white roses in a white vase" style="left:754px;top:1330px;background:linear-gradient(180deg,#c9c9c9 0%,#d8a3a8 45%,#bdbdbd 100%)"></div>
  <div class="card-name" style="left:754px;top:1592px">Alluring Red</div>
  <div class="price" style="left:760px;top:1621px"><small>$</small>12.65</div>

  <!-- row 2 -->
  <div class="card-img" role="img" aria-label="Mixed roses in a burlap wrapped pot" style="left:183px;top:1702px;background:linear-gradient(180deg,#d9d9d7 0%,#d5c39a 50%,#8e8e8c 100%)"></div>
  <div class="card-name" style="left:183px;top:1962px">Let a Thousand Flowers Bloom</div>
  <div class="price" style="left:189px;top:1991px"><small>$</small>15.68</div>

  <div class="card-img" role="img" aria-label="Magenta orchids in a glass vase" style="left:468px;top:1702px;background:linear-gradient(180deg,#f7f7f7 0%,#e06ad0 45%,#efeeea 100%)"></div>
  <div class="card-name" style="left:468px;top:1962px">Garden Box</div>
  <div class="price" style="left:474px;top:1991px"><small>$</small>19.30</div>

  <div class="card-img" role="img" aria-label="White daisies in a vase on a bright yellow background" style="left:754px;top:1702px;background:linear-gradient(180deg,#fbb31a 0%,#f4e3c4 50%,#f9a91b 100%)"></div>
  <div class="card-name" style="left:754px;top:1962px">Alluring White</div>
  <div class="price" style="left:760px;top:1991px"><small>$</small>16.95</div>

  <!-- stars -->
  <svg width="0" height="0" style="position:absolute"><defs><polygon id="star" points="8,1 10,6 15.5,6.2 11.2,9.6 12.8,15 8,11.8 3.2,15 4.8,9.6 0.5,6.2 6,6"/></defs></svg>
  <div class="stars" style="left:349px;top:1624px"><svg width="92" height="16" viewBox="0 0 92 16"><use href="#star" fill="#f4b400"/><use href="#star" x="18.5" fill="#f4b400"/><use href="#star" x="37" fill="#f4b400"/><use href="#star" x="55.5" fill="#f4b400"/><use href="#star" x="74" fill="#d6d6d6"/></svg></div>
  <div class="stars" style="left:634px;top:1624px"><svg width="92" height="16" viewBox="0 0 92 16"><use href="#star" fill="#f4b400"/><use href="#star" x="18.5" fill="#f4b400"/><use href="#star" x="37" fill="#f4b400"/><use href="#star" x="55.5" fill="#f4b400"/><use href="#star" x="74" fill="#d6d6d6"/></svg></div>
  <div class="stars" style="left:919px;top:1624px"><svg width="92" height="16" viewBox="0 0 92 16"><use href="#star" fill="#f4b400"/><use href="#star" x="18.5" fill="#f4b400"/><use href="#star" x="37" fill="#f4b400"/><use href="#star" x="55.5" fill="#f4b400"/><use href="#star" x="74" fill="#d6d6d6"/></svg></div>
  <div class="stars" style="left:349px;top:1994px"><svg width="92" height="16" viewBox="0 0 92 16"><use href="#star" fill="#f4b400"/><use href="#star" x="18.5" fill="#f4b400"/><use href="#star" x="37" fill="#f4b400"/><use href="#star" x="55.5" fill="#f4b400"/><use href="#star" x="74" fill="#d6d6d6"/></svg></div>
  <div class="stars" style="left:634px;top:1994px"><svg width="92" height="16" viewBox="0 0 92 16"><use href="#star" fill="#f4b400"/><use href="#star" x="18.5" fill="#f4b400"/><use href="#star" x="37" fill="#f4b400"/><use href="#star" x="55.5" fill="#f4b400"/><use href="#star" x="74" fill="#d6d6d6"/></svg></div>
  <div class="stars" style="left:919px;top:1994px"><svg width="92" height="16" viewBox="0 0 92 16"><use href="#star" fill="#f4b400"/><use href="#star" x="18.5" fill="#f4b400"/><use href="#star" x="37" fill="#f4b400"/><use href="#star" x="55.5" fill="#f4b400"/><use href="#star" x="74" fill="#d6d6d6"/></svg></div>

  <div class="btn" style="left:527px;top:2078px;width:140px;height:50px">View More</div>
</section>

<!-- EVENTS -->
<section class="abs" style="left:0;top:2218px;width:1200px;height:491px;background:var(--band)"></section>
<div class="eyebrow" style="left:183px;top:2304px">Events</div>
<h2 class="h-title" style="left:183px;top:2330px;font-size:29px;line-height:42px">Your Favorite<br>Florist</h2>
<p class="para" style="left:183px;top:2436px;width:200px">Ut enim ad minim veniam, quis nostrud exerci tation ullamco laboris nisi ut aliquip ex ea commodo consequat.</p>
<div class="circle-btn" style="left:183px;top:2588px;background:var(--blush)"><svg width="8" height="12" viewBox="0 0 8 12" fill="none" stroke="#555" stroke-width="1.3"><path d="M6 1L1 6l5 5"/></svg></div>
<div class="circle-btn" style="left:238px;top:2588px;background:#fff"><svg width="8" height="12" viewBox="0 0 8 12" fill="none" stroke="#555" stroke-width="1.3"><path d="M2 1l5 5-5 5"/></svg></div>

<div class="ev-img" role="img" aria-label="Red and white rose wedding bouquet" style="left:418px;top:2308px;background:linear-gradient(160deg,#e8e4df 0%,#c91f24 45%,#f1ece8 100%)"></div>
<div class="ev-name" style="left:425px;top:2557px">Wedding Bouquet</div>
<div class="ev-desc" style="left:425px;top:2584px">Quis ipsum suspendisse ultrices gravida risus.</div>

<div class="ev-img" role="img" aria-label="White rose birthday bouquet" style="left:633px;top:2308px;background:linear-gradient(160deg,#e9e9e9 0%,#f7f6f2 50%,#cfd3c8 100%)"></div>
<div class="ev-name" style="left:640px;top:2557px">Birthday Bouquet</div>
<div class="ev-desc" style="left:640px;top:2584px">Quis ipsum suspendisse ultrices commodo viverra maecenas.</div>

<div class="ev-img" role="img" aria-label="Peach and orange rose anniversary bouquet" style="left:847px;top:2308px;background:linear-gradient(160deg,#e6ddd6 0%,#f0a37a 45%,#d99584 100%)"></div>
<div class="ev-name" style="left:854px;top:2557px">Anniversary Bouquet</div>
<div class="ev-desc" style="left:854px;top:2584px">Quis ipsum suspendisse ultrices commodo.</div>

<div class="ev-img" role="img" aria-label="White rose arrangement" style="left:1060px;top:2308px;width:140px;background:linear-gradient(160deg,#f4f4ef 0%,#e9eedb 50%,#9fb28b 100%)"></div>
<div class="ev-name" style="left:1067px;top:2557px">Death Bouquet</div>
<div class="ev-desc" style="left:1067px;top:2584px;width:133px">Quis ipsum suspendisse commodo.</div>

<!-- TESTIMONIAL -->
<div class="eyebrow" style="left:531px;top:2796px">Testimonial</div>
<h2 class="h-title" style="left:0;width:1200px;text-align:center;top:2826px;font-size:29px">Let's Have A Look What Our Customer Says</h2>

<div class="pink-block" style="left:390px;top:2979px;width:57px;height:71px"></div>
<div class="photo" role="img" aria-label="Bride holding a white bouquet" style="left:468px;top:2945px;width:82px;height:106px;background:linear-gradient(180deg,#d5d3cf,#efeae8)"></div>
<div class="pink-block" style="left:176px;top:3099px;width:56px;height:73px"></div>
<div class="photo" role="img" aria-label="Bride in a pink gown holding a bouquet" style="left:255px;top:3073px;width:213px;height:278px;background:linear-gradient(180deg,#5d8a5e 0%,#d5a8b4 50%,#eab9c6 100%)"></div>
<div class="photo" role="img" aria-label="Couple on their wedding day" style="left:112px;top:3195px;width:120px;height:156px;background:linear-gradient(180deg,#e8e4df,#c4b8ae)"></div>
<div class="photo" role="img" aria-label="Bride in a lilac lace dress" style="left:489px;top:3195px;width:121px;height:156px;background:linear-gradient(180deg,#d9d4cf,#a8a4c8)"></div>
<div class="pink-block" style="left:255px;top:3372px;width:57px;height:77px"></div>
<div class="pink-block" style="left:489px;top:3372px;width:57px;height:77px"></div>

<div class="circle-btn" style="left:645px;top:3050px;width:55px;height:55px;background:#fff;box-shadow:0 4px 16px rgba(230,150,180,.25)"><span class="serif" style="font-size:34px;color:var(--blush);line-height:1;margin-top:14px">”</span></div>
<p class="para" style="left:658px;top:3170px;width:318px">Ut enim ad minim veniam, quis nostrud exerci tation ullamco laboris nisi ut aliquip ex ea commodo cons equat. Duis aute irure dolor in reprehenderit in volup tate velit esse cillum.</p>
<div class="abs serif" style="left:700px;width:268px;text-align:right;top:3283px;font-size:15px;color:#555">- Mara Ellison</div>
<div class="circle-btn" style="left:659px;top:3357px;background:#fff;box-shadow:0 2px 8px rgba(0,0,0,.06)"><svg width="8" height="12" viewBox="0 0 8 12" fill="none" stroke="#555" stroke-width="1.3"><path d="M6 1L1 6l5 5"/></svg></div>
<div class="circle-btn" style="left:712px;top:3357px;background:var(--blush)"><svg width="8" height="12" viewBox="0 0 8 12" fill="none" stroke="#555" stroke-width="1.3"><path d="M2 1l5 5-5 5"/></svg></div>

<!-- CONTACT -->
<section class="abs" style="left:0;top:3537px;width:1200px;height:421px;background:var(--clay)"></section>
<div class="photo" role="img" aria-label="Pink and white tulips wrapped in kraft paper with a pink ribbon" style="left:656px;top:3537px;width:544px;height:421px;background:radial-gradient(ellipse at 60% 45%,#e9a5bd 0%,#d9b3a6 45%,#ecccbf 75%)"></div>
<div class="eyebrow" style="left:183px;top:3623px">Contact Us</div>
<h2 class="h-title" style="left:183px;top:3650px;font-size:29px">Feel Free To Contact</h2>
<div class="circle-btn" style="left:183px;top:3720px;width:47px;height:47px;background:#fff"><svg width="18" height="18" viewBox="0 0 18 18" fill="none" stroke="#333" stroke-width="1.3"><path d="M4 1.5l3 3.5-1.8 2a10 10 0 0 0 5.8 5.8l2-1.8 3.5 3-1.5 2.5C9 16.5 1.5 9 1.5 3.5z"/></svg></div>
<div class="abs" style="left:255px;top:3733px;font-size:14.5px;line-height:30px;color:#222">+(61) 2140 558 312<br>+(61) 2140 771 905</div>
<div class="circle-btn" style="left:183px;top:3805px;width:47px;height:47px;background:#fff"><svg width="18" height="14" viewBox="0 0 18 14" fill="none" stroke="#333" stroke-width="1.3"><rect x="1" y="1" width="16" height="12"/><path d="M1 1l8 6 8-6"/></svg></div>
<div class="abs" style="left:255px;top:3820px;font-size:14.5px;line-height:30px;color:#222">hello@fernandvale.com<br>orders@fernandvale.com</div>

<!-- NEWSLETTER -->
<h2 class="h-title" style="left:183px;top:4058px;font-size:29px">Subscribe Our Newsletter</h2>
<div class="abs" style="left:569px;top:4050px;width:443px;height:53px;background:#fff;box-shadow:0 4px 18px rgba(0,0,0,.07)"></div>
<div class="abs" style="left:585px;top:4069px;font-size:12px;color:#bbb">Enter your email address</div>
<div class="btn" style="left:872px;top:4050px;width:140px;height:53px">Subscribe</div>

<!-- FOOTER -->
<footer class="footer">
  <div class="f-head" style="left:183px;top:74px">Quick Links</div>
  <div class="f-link" style="left:183px;top:123px">Home</div>
  <div class="f-link" style="left:183px;top:166px">About Us</div>
  <div class="f-link" style="left:183px;top:208px">Bouquets</div>
  <div class="f-link" style="left:183px;top:251px">Events</div>
  <div class="f-link" style="left:324px;top:123px">Testimonial</div>
  <div class="f-link" style="left:324px;top:166px">Contact Us</div>
  <div class="f-link" style="left:324px;top:208px">Trams &amp; Condition</div>
  <div class="f-link" style="left:324px;top:251px">Privacy &amp; Policy</div>

  <div class="brand" style="left:532px;top:125px;color:#fff;font-size:28px"><span class="dot" style="border-color:#fff"></span>Fern&amp;Vale</div>

  <div class="f-head" style="left:752px;top:74px">Contact</div>
  <svg class="abs" style="left:752px;top:121px" width="12" height="12" viewBox="0 0 18 18" fill="none" stroke="#fff" stroke-width="1.5"><path d="M4 1.5l3 3.5-1.8 2a10 10 0 0 0 5.8 5.8l2-1.8 3.5 3-1.5 2.5C9 16.5 1.5 9 1.5 3.5z"/></svg>
  <div class="f-link" style="left:773px;top:119px;line-height:23px">+(61) 2140 558 312<br>+(61) 2140 771 905</div>
  <svg class="abs" style="left:752px;top:181px" width="13" height="10" viewBox="0 0 18 14" fill="none" stroke="#fff" stroke-width="1.5"><rect x="1" y="1" width="16" height="12"/><path d="M1 1l8 6 8-6"/></svg>
  <div class="f-link" style="left:773px;top:177px;line-height:23px">hello@fernandvale.com<br>orders@fernandvale.com</div>
  <span class="abs" style="left:755px;top:250px;width:9px;height:9px;border-radius:50%;background:#fff"></span>
  <span class="abs" style="left:778px;top:250px;width:9px;height:9px;border-radius:50%;background:#fff"></span>
  <span class="abs" style="left:801px;top:250px;width:9px;height:9px;border-radius:50%;background:#fff"></span>

  <div class="abs" style="left:183px;top:296px;width:833px;height:1px;background:#333"></div>
  <div class="abs" style="left:700px;width:316px;text-align:right;top:306px;font-size:10px;color:#ddd">© copyright fern&amp;vale 2021 | all right reserved</div>
</footer>

</body>
</html>
```